Wow, Spring Is Near!

I am a mobile weight loss consultant. I have partnered up with the Vitality Kickoff scheme which is based on real food. I travel to my clients at work or at home or in my own home office. My target audience is mothers -especial younger mothers with school kids and its time for my clients to focus on themselves they are worth it. I have over 10 years experience as a weight loss consultant. No contracts and no risk and i want them directed to my Facebook page BrightpathWellnessGuide or call me on 0439582706.

I am looking for a flyer to attached to his brochure early Feb for the mothers with all the kids going to back to school. ( i will attach so you can see it).
I have attached VK advertising with the girl and the banana. I do like the vk official partner somewhere on it?? I like the back drop as the girl with a banana or a mum and kids ?? I don't know

Limitied places so be quick

I have attached my logo as well.

Any questions plz ask I just need something when mothers see it, they will look twice and just chuck it in the bin??
Thank you
Maren

Just leaning how to use sketch hive so I have updated my information to help you. Thank you

Reason: I am getting many great designs. I am currently on holidays and get home tomorrow and would like a couple of days to get my friends options etc before I decide. Thank you to all designers

Target Market(s)

mothers, especially young mums with kids at school- which will just be starting back at school in February.

Industry/Entity Type

Advertising

Requirements
Must have
• somehow :-
- no contracts with no risk
- experienced
- i go to them at home or work
- real food
Should not have
• The word "diet"

```html
<!DOCTYPE html>
<html lang="en">
<head>
<meta charset="utf-8">
<title>Brightpath Wellness Guide – Flyer</title>
<link rel="stylesheet" href="https://fonts.googleapis.com/css2?family=Oswald:wght@500;700&family=Lato:wght@700;900&display=swap">
<style>
  :root {
    --sky: #4fa3d9;
    --sky-deep: #3b8fc8;
    --sky-soft: #7dbde6;
    --sun: #fcd54a;
    --coral: #ef6b70;
    --lime: #b7d94a;
    --white: #ffffff;
    --paper: #f7f7f5;
    --ink-blue: #2f86c6;
  }
  * { box-sizing: border-box; margin: 0; padding: 0; }
  html, body { width: 1200px; height: 900px; overflow: hidden; background: var(--paper); }
  .flyer {
    position: relative;
    width: 1200px;
    height: 900px;
    overflow: hidden;
    background: linear-gradient(160deg, var(--sky-soft) 0%, var(--sky) 45%, var(--sky-deep) 100%);
    font-family: "Oswald", "Arial Narrow", sans-serif;
  }
  .photo-side { position: absolute; left: 0; top: 0; width: 560px; height: 900px; }
  .badge-experienced { position: absolute; left: 200px; top: 16px; width: 240px; height: 240px; }
  .badge-realfood { position: absolute; left: 332px; top: 622px; width: 240px; height: 240px; }
  .brand {
    position: absolute; left: 640px; top: 120px; width: 460px;
    display: flex; align-items: center; justify-content: center; gap: 14px;
  }
  .brand-dot { width: 26px; height: 26px; border-radius: 50%; background: var(--white); flex: none; }
  .brand-name {
    font-family: "Lato", sans-serif; font-weight: 900; font-size: 30px; color: var(--white);
  }
  .headline {
    position: absolute; left: 560px; width: 640px; text-align: center;
    font-weight: 700; line-height: 1; text-shadow: 2px 3px 4px rgba(0,0,0,0.25);
    letter-spacing: 1px;
  }
  .headline--top { top: 262px; font-size: 80px; color: var(--coral); }
  .headline--bottom { top: 350px; font-size: 80px; color: var(--white); }
  .band {
    position: absolute; background: var(--sun);
  }
  .band--offer { left: 540px; top: 470px; width: 660px; height: 150px; transform: rotate(-1deg); }
  .band--call { left: 600px; top: 805px; width: 600px; height: 95px; }
  .offer-text {
    position: absolute; left: 560px; width: 640px; text-align: center; font-weight: 700; line-height: 1;
  }
  .offer-text--main { top: 495px; font-size: 32px; color: var(--ink-blue); }
  .offer-text--sub { top: 537px; font-size: 27px; color: var(--coral); font-weight: 500; }
  .promise {
    position: absolute; left: 560px; width: 640px; text-align: center; font-weight: 700; line-height: 1;
  }
  .promise--lead { top: 638px; font-size: 38px; color: var(--lime); text-shadow: 1px 2px 3px rgba(0,0,0,0.2); }
  .promise--lead .accent { color: var(--coral); }
  .promise--main { top: 684px; font-size: 60px; color: var(--white); text-shadow: 2px 3px 4px rgba(0,0,0,0.25); }
  .call {
    position: absolute; right: 56px; top: 830px;
    font-family: "Lato", sans-serif; font-weight: 900; font-size: 32px; color: var(--coral);
  }
  .call .number { color: var(--ink-blue); }
</style>
</head>
<body>
<main class="flyer">
  <svg class="photo-side" viewBox="0 0 560 900" role="img" aria-label="Photo of green and red apples wrapped with a measuring tape on a white surface">
    <defs>
      <linearGradient id="fruitTone" x1="0" y1="0" x2="1" y2="1">
        <stop offset="0" stop-color="#ffffff"/>
        <stop offset="0.35" stop-color="#f4ece8"/>
        <stop offset="0.55" stop-color="#d9584a"/>
        <stop offset="0.75" stop-color="#c9423a"/>
        <stop offset="1" stop-color="#e9e6e2"/>
      </linearGradient>
    </defs>
    <path fill="url(#fruitTone)" d="M0 0 H478 L470 40 L486 90 L472 140 L490 200 L474 260 L492 330 L476 400 L494 470 L478 540 L496 610 L480 680 L498 750 L482 820 L492 900 H0 Z"/>
  </svg>

  <svg class="badge-experienced" viewBox="0 0 240 240" aria-label="Experienced">
    <circle cx="120" cy="120" r="112" fill="none" stroke="var(--ink-blue)" stroke-width="6"/>
    <circle cx="120" cy="120" r="96" fill="none" stroke="var(--ink-blue)" stroke-width="3"/>
    <g transform="rotate(-25 120 120)">
      <rect x="20" y="96" width="200" height="48" fill="var(--white)" stroke="var(--ink-blue)" stroke-width="4"/>
      <text x="120" y="133" text-anchor="middle" font-family="Oswald, sans-serif" font-weight="700" font-size="36" fill="var(--ink-blue)">EXPERIENCED</text>
    </g>
  </svg>

  <svg class="badge-realfood" viewBox="0 0 240 240" aria-label="Real food">
    <circle cx="120" cy="120" r="112" fill="none" stroke="var(--coral)" stroke-width="6"/>
    <circle cx="120" cy="120" r="98" fill="var(--white)" stroke="var(--coral)" stroke-width="10"/>
    <text x="120" y="118" text-anchor="middle" font-family="Oswald, sans-serif" font-weight="700" font-size="54" fill="var(--ink-blue)">REAL</text>
    <text x="120" y="172" text-anchor="middle" font-family="Oswald, sans-serif" font-weight="700" font-size="54" fill="var(--coral)">FOOD</text>
  </svg>

  <div class="brand">
    <span class="brand-dot"></span>
    <span class="brand-name">BrightpathWellnessGuide</span>
  </div>

  <h1 class="headline headline--top">NO CONTRACTS</h1>
  <p class="headline headline--bottom">WITH NO RISK</p>

  <div class="band band--offer"></div>
  <p class="offer-text offer-text--main">MOBILE WEIGHT LOSS CONSULTANT- OFFERING</p>
  <p class="offer-text offer-text--sub">CONSOLATIONS AT YOUR HOME OR WORK</p>

  <p class="promise promise--lead">YOU WILL ONLY <span class="accent">LOSE THE WEIGHT</span></p>
  <p class="promise promise--main">YOU WANT TO LOSE</p>

  <div class="band band--call"></div>
  <p class="call">CALL US <span class="number">0439582706</span></p>
</main>
</body>
</html>
```